Bright Anchor Tools and Building Supply Inc. (Rebranding)

Target Market(s)

mainly people who do DIY, and also construction companies.

Industry/Entity Type

Construction

Contact Information for Business Card

418 R. Velasco St. Brgy. 164 Sta. Lucia Manila, Philippines 1003
(02) 861-4097
www.bat.example
brightanchortools@mailbox.example

Number of Pages Required

5+ page

Font styles to use
Sans Serif

Colors
f37122
f78f20

Requirements
Must have
• to RETAIN the current logo used.
Nice to have
• ideas on how to apply the current logos to different promotional items
Should not have
• DO NOT change the Current Logo

```html
<!DOCTYPE html>
<html lang="en">
<head>
<meta charset="utf-8">
<title>Bright Anchor Tools and Building Supply Inc. – Stationery</title>
<link rel="stylesheet" href="https://fonts.googleapis.com/css2?family=Arimo:wght@400;700&family=Lato:wght@400;700&display=swap">
<style>
  :root {
    --brand-orange: #f37122;
    --brand-orange-light: #f78f20;
    --paper-white: #ffffff;
    --backdrop: #ece4d6;
    --flap-shadow: rgba(0, 0, 0, 0.12);
    --rule-grey: #9a9a9a;
  }
  * { box-sizing: border-box; margin: 0; padding: 0; }
  html, body { width: 1200px; height: 720px; overflow: hidden; }
  body {
    background: var(--backdrop);
    font-family: "Arimo", Arial, sans-serif;
    color: var(--paper-white);
  }
  .canvas { position: relative; width: 1200px; height: 720px; }
  .piece {
    position: absolute;
    background: var(--brand-orange);
    overflow: hidden;
    box-shadow: 0 2px 6px rgba(0, 0, 0, 0.15);
  }
  .piece > svg.swoosh { position: absolute; inset: 0; width: 100%; height: 100%; }

  /* Wordmark */
  .wordmark {
    position: absolute;
    font-family: "Arimo", Arial, sans-serif;
    font-weight: 700;
    color: var(--paper-white);
    line-height: 1;
    text-transform: uppercase;
    white-space: nowrap;
  }
  .wordmark__name { display: block; letter-spacing: 0.01em; }
  .wordmark__line { display: block; font-size: 0.3em; letter-spacing: 0.08em; margin-top: 0.35em; }

  /* Letterhead */
  .letterhead { left: 76px; top: 110px; width: 352px; height: 497px; }
  .letterhead .wordmark { left: 38px; top: 40px; font-size: 17px; }
  .letterhead__watermark {
    position: absolute; left: 58px; top: 205px;
    font-weight: 700; font-size: 28px; text-transform: uppercase;
    color: rgba(255, 255, 255, 0.09); white-space: nowrap;
  }
  .letterhead__body {
    position: absolute; left: 39px; top: 80px; width: 278px;
    font-size: 5.4px; line-height: 1.32;
  }
  .letterhead__body h2 { font-size: 5.4px; font-weight: 400; margin-top: 7px; }
  .letterhead__footer {
    position: absolute; left: 46px; bottom: 71px;
    font-size: 5.4px;
  }

  /* Business cards */
  .card { top: 109px; width: 151px; height: 84px; }
  .card--front { left: 460px; }
  .card--front .wordmark { right: 10px; top: 26px; font-size: 10.5px; }
  .card--back { left: 650px; }
  .card--back .wordmark { left: 14px; top: 17px; font-size: 7.5px; }
  .card__person { position: absolute; right: 12px; top: 12px; text-align: left; font-family: "Lato", Arial, sans-serif; }
  .card__name { font-size: 8px; font-weight: 400; }
  .card__role { font-size: 4.4px; font-weight: 700; margin-top: 2px; }
  .card__contact {
    position: absolute; left: 89px; top: 40px;
    font-family: "Lato", Arial, sans-serif; font-size: 4.6px; font-weight: 700; line-height: 1.55;
    white-space: nowrap;
  }

  /* Envelope */
  .envelope { left: 449px; width: 369px; height: 184px; }
  .envelope--front { top: 216px; }
  .envelope--front .wordmark { left: 35px; top: 68px; font-size: 15px; }
  .envelope__window {
    position: absolute; left: 186px; top: 78px; width: 150px; height: 74px;
    background: var(--paper-white); border: 1px solid #e2e2e2;
  }
  .envelope__window .address-rule {
    position: absolute; left: 17px; right: 17px; height: 1px; background: var(--rule-grey);
  }
  .envelope--back { top: 421px; }

  /* Notepad */
  .notepad { left: 838px; top: 253px; width: 251px; height: 352px; overflow: visible; }
  .notepad .wordmark { left: 0; right: 0; top: 128px; font-size: 17px; text-align: center; }
  .notepad__binding { position: absolute; left: 10px; top: -14px; width: 231px; height: 28px; overflow: visible; }
</style>
</head>
<body>
<main class="canvas">

  <!-- Letterhead -->
  <article class="piece letterhead">
    <div class="wordmark"><span class="wordmark__name">Bright Anchor</span><span class="wordmark__line">Tools &amp; Building Supply Inc.</span></div>
    <div class="letterhead__watermark" aria-hidden="true">Bright Anchor</div>
    <div class="letterhead__body">
      <p>Bright Anchor Tools and Building Supply Inc. serves home builders, weekend makers and contractors across Manila with dependable hardware, lumber, fasteners and power tools. Our counters open early so crews can load up before the first pour, and our staff can help match every job to the right part.</p>
      <h2>Tools and hardware</h2>
      <p>Hand tools, drills, saws, levels and safety gear from trusted makers, kept in stock and ready for pickup or delivery.</p>
      <h2>Building materials</h2>
      <p>Cement, steel bars, plywood, roofing, pipes and paint, cut and bundled to order for sites of any size.</p>
      <h2>Project support</h2>
      <p>Bring your plans and our team will list quantities, compare costs and schedule drops to your site on time.</p>
      <h2>Trade accounts</h2>
      <p>Construction firms can open an account for volume pricing, monthly billing and a dedicated order line.</p>
      <h2>Do it yourself</h2>
      <p>Weekend builders get free advice, simple guides and rentals for the bigger jobs around the house.</p>
    </div>
    <div class="letterhead__footer">www.bat.example</div>
  </article>

  <!-- Business card front -->
  <article class="piece card card--front">
    <svg class="swoosh" viewBox="0 0 151 84" preserveAspectRatio="none" aria-hidden="true">
      <path d="M0 46 C40 66 95 86 140 84 L0 84 Z" fill="var(--paper-white)"/>
    </svg>
    <div class="wordmark"><span class="wordmark__name">Bright Anchor</span><span class="wordmark__line">Tools &amp; Building Supply Inc.</span></div>
  </article>

  <!-- Business card back -->
  <article class="piece card card--back">
    <svg class="swoosh" viewBox="0 0 151 84" preserveAspectRatio="none" aria-hidden="true">
      <path d="M0 46 C40 66 95 86 140 84 L0 84 Z" fill="var(--paper-white)"/>
    </svg>
    <div class="wordmark"><span class="wordmark__name">Bright Anchor</span><span class="wordmark__line">Tools &amp; Building Supply Inc.</span></div>
    <div class="card__person">
      <div class="card__name">Mara Quintos</div>
      <div class="card__role">Co-Founder &amp; CEO</div>
    </div>
    <div class="card__contact">
      <div>T:&nbsp; (02) 861-4097</div>
      <div>M:&nbsp; mara@bat.example</div>
      <div>W:&nbsp; www.bat.example</div>
    </div>
  </article>

  <!-- Envelope front -->
  <article class="piece envelope envelope--front">
    <svg class="swoosh" viewBox="0 0 369 184" preserveAspectRatio="none" aria-hidden="true">
      <path d="M0 82 C110 140 230 178 369 158 L369 184 L0 184 Z" fill="var(--paper-white)"/>
      <path d="M170 184 C270 180 340 165 369 138 L369 184 Z" fill="var(--brand-orange)"/>
    </svg>
    <div class="wordmark"><span class="wordmark__name">Bright Anchor</span><span class="wordmark__line">Tools &amp; Building Supply Inc.</span></div>
    <div class="envelope__window">
      <span class="address-rule" style="top:38px"></span>
      <span class="address-rule" style="top:46px"></span>
      <span class="address-rule" style="top:54px"></span>
      <span class="address-rule" style="top:62px"></span>
    </div>
  </article>

  <!-- Envelope back -->
  <article class="piece envelope envelope--back">
    <svg class="swoosh" viewBox="0 0 369 184" preserveAspectRatio="none" aria-hidden="true">
      <path d="M4 0 L8 52 Q9 56 14 56 L355 56 Q360 56 361 52 L365 0 Z" fill="var(--brand-orange-light)" opacity="0.25"/>
      <path d="M4 0 L8 52 Q9 56 14 56 L355 56 Q360 56 361 52 L365 0" fill="none" stroke="var(--flap-shadow)" stroke-width="1.2"/>
    </svg>
  </article>

  <!-- Notepad -->
  <article class="piece notepad">
    <svg class="notepad__binding" viewBox="0 0 231 28" aria-hidden="true">
      <g fill="none" stroke="#555" stroke-width="2.4">
        <path d="M10 22 V8 a4 4 0 0 1 8 0 V22"/>
        <path d="M34 22 V8 a4 4 0 0 1 8 0 V22"/>
        <path d="M58 22 V8 a4 4 0 0 1 8 0 V22"/>
        <path d="M82 22 V8 a4 4 0 0 1 8 0 V22"/>
        <path d="M106 22 V8 a4 4 0 0 1 8 0 V22"/>
        <path d="M130 22 V8 a4 4 0 0 1 8 0 V22"/>
        <path d="M154 22 V8 a4 4 0 0 1 8 0 V22"/>
        <path d="M178 22 V8 a4 4 0 0 1 8 0 V22"/>
        <path d="M202 22 V8 a4 4 0 0 1 8 0 V22"/>
      </g>
      <g fill="#2b2b2b">
        <circle cx="14" cy="24" r="3"/><circle cx="38" cy="24" r="3"/><circle cx="62" cy="24" r="3"/>
        <circle cx="86" cy="24" r="3"/><circle cx="110" cy="24" r="3"/><circle cx="134" cy="24" r="3"/>
        <circle cx="158" cy="24" r="3"/><circle cx="182" cy="24" r="3"/><circle cx="206" cy="24" r="3"/>
      </g>
    </svg>
    <div class="wordmark"><span class="wordmark__name">Bright Anchor</span><span class="wordmark__line">Tools &amp; Building Supply Inc.</span></div>
  </article>

</main>
</body>
</html>
```